VELMARO CREST ADVISORY

Need a Boucher designed with vibrant colours and well aligned. The content is there in the word file what I have attached. The heading and the subject of each paragraph has to be separated by designing accordingly. I would appreciate if nice hd pictures of stock market/trading/forex/consulting can be accommodated with this.

Target Market(s)

traders, stock traders, business entrepreneurs

Font styles to use
Sans Serif

Requirements
Must have
• Images from stock market and charts
Nice to have
• I want it to look elegant as this goes to the trading community.
Should not have
• Don't want anything that looks goody or fashionable since its a professional broucher.

```html
<!DOCTYPE html>
<html lang="en">
<head>
<meta charset="utf-8">
<title>Velmaro Crest Advisory – Brochure Spread</title>
<link href="https://fonts.googleapis.com/css2?family=Jost:ital,wght@0,400;0,600;0,700;1,400&display=swap" rel="stylesheet">
<style>
  :root{
    --backdrop:#444444;
    --paper:#ffffff;
    --ink:#222222;
    --accent:#1b9ad6;
    --brand-grey:#555a60;
    --tone-top:#ddd9a6;
    --tone-mid:#c8d3b4;
    --tone-low:#8fb3b8;
    --tone-base:#d6e2e3;
  }
  *{box-sizing:border-box;margin:0;padding:0}
  html,body{width:1200px;height:1200px;overflow:hidden;background:var(--backdrop)}
  body{position:relative;font-family:"Jost",sans-serif;color:var(--ink)}
  .page{position:absolute;top:203px;width:561px;height:793px;overflow:hidden}
  .page--left{left:27px;background:var(--paper)}
  .page--right{left:611px}
  .hero-photo{position:absolute;inset:0;
    background:
      radial-gradient(ellipse 40% 45% at 50% 78%, rgba(40,70,95,.75), rgba(40,70,95,0) 70%),
      linear-gradient(180deg,var(--tone-top) 0%,var(--tone-mid) 45%,var(--tone-low) 72%,var(--tone-base) 100%);}
  .tab{position:absolute;left:529px;top:23px;width:32px;height:49px;background:var(--accent)}
  .brand{position:absolute;left:330px;top:34px;display:flex;align-items:center;gap:8px}
  .brand-mark{width:22px;height:22px;background:var(--accent)}
  .brand-name{font-weight:600;font-size:17px;letter-spacing:.5px;color:var(--brand-grey)}
  .column{position:absolute;font-size:10.4px;line-height:13.5px;text-align:justify;hyphens:auto}
  .column p{margin-bottom:3.5px}
  .column ul{list-style:none}
  .column li{position:relative;padding-left:14px;margin-bottom:3px}
  .column li::before{content:"•";position:absolute;left:0;font-size:8px}
  .lead{color:var(--accent);font-weight:700}
  .quote{font-weight:700;font-style:italic}
  .note{font-style:italic}
  .left-a{left:52px;top:98px;width:221px}
  .left-b{left:288px;top:98px;width:220px}
  .right-a{left:53px;top:58px;width:220px}
  .right-b{left:289px;top:58px;width:219px}
  .signoff{position:absolute;left:404px;top:364px;font-size:10.4px;line-height:12.5px}
  .signoff strong{font-weight:700}
</style>
</head>
<body>
  <section class="page page--left">
    <div class="tab"></div>
    <div class="brand"><span class="brand-mark"></span><span class="brand-name">VELMARO CREST</span></div>

    <div class="column left-a">
      <ul>
        <li>Undergo the process – To become a trader, its important to develop all the skills that are required to be a pro trader. The Psychology and mindset of the trader plays a very important role in becoming successful in this business. Believe in the process.</li>
        <li>Strategy &amp; risk management – All you need is a strategy with a proven track record, backed by solid risk management principles. The only way to excel in any profession is to learn from someone who is already doing what you intend to do. Approach someone who can teach you the key trading skills.</li>
      </ul>
      <p>Know thyself – Your nature would have a lot of impact on your trading results. If you are impulsive by nature and end up buying things that you don't need every time you go shopping, chances are very high that you would end up being impulsive in trading too; this is extremely dangerous. Similarly, if you are normally unorganized and lack discipline in other walks of life, chances are high that you will continue with that habit into your trading profession as well. These aspects seem trivial, but you may end up paying a heavy price if you don't set them right in the beginning itself.</p>
      <p><span class="lead">Trading is an amazing profession with unparalleled advantages.</span> However, you have to give yourself some time, learn the craft, be patient - only then the fruits will follow. My experience as a trader as well tells me that whoever follows the process correctly eventually succeeds in achieving what they desire to.</p>
      <p>In case you are looking at trading seriously, and you want to learn from the professionals, know the strategy that has consistently worked across market cycles, gain insights as to how the “big boys” trade, We would encourage you to register for one of our Programs, It could be one of the best financial decisions you will ever take in your life!</p>
    </div>

    <div class="column left-b">
      <p><span class="lead">Trading has to be the best business in the world</span> — You have no employees, no bosses, no offices to rent and no product to sell. As an independent trader, the set-up costs and running costs are low; all you need is a computer, a desk, and an inexpensive trading software. When trading is done thoughtfully and efficiently as a proper business – controlling the risks and managing the expectations — profit margins are <em>high</em>. Profit margins for trading businesses are among the highest in the world — no wonder why the investment bankers are so flush with cash.</p>
      <p>In many ways, trading really is the perfect business. One thing, however, is as critical for that business as for any other company – and that is <em>capital</em>.</p>
      <p>Without a sizeable amount of trading capital, it doesn't matter how well you trade and how disciplined you are – the returns you make will not be life-changing.</p>
      <p>What new traders usually do to overcome their small account sizes is to use high leverage on their accounts and take a crazy amount of risk – often as much as 5-10% per trade. That kind of trading inevitably ends up with blown accounts and shattered dreams.</p>
      <p>Lack of capital is one of the main reasons that prevents traders pursuing their trading careers. Countless times have I heard people say:</p>
      <p class="quote">"If only I had money, I would trade for a living."</p>
      <p>or</p>
      <p class="quote">"My account is too small to trade effectively"</p>
      <p>These arguments are no longer valid! <span class="lead">For good traders, funding is never an issue and getting funded is now easier than ever.</span></p>
      <p>“Serious money will not come from trading your own money but from managing other</p>
    </div>
  </section>

  <section class="page page--right">
    <div class="hero-photo" role="img" aria-label="Photo of a businessman in a suit crouched in a sprinter's starting position on a softly lit floor"></div>

    <div class="column right-a">
      <p>people's money!”</p>
      <p>All the major central bank's money-printing exercises over the last decade have resulted in so much money being available, money that people are investing not only in the stock markets and real estate, but also in <strong>talented traders</strong>.</p>
      <p>To get funded, all you have to do is prove that you can trade with discipline and in a consistent way – even if it's on a small account!</p>
      <p>Investors, in particular, like traders that use objective trading systems with well-structured and automated approaches (bots). This is because trading with bots and objective trading strategies means that you are not subject to the emotional rollercoaster that is often derailing even the most talented discretionary traders who are using subjective trading strategies.</p>
      <p>If you can show solid and consistent trading where you manage your risk and achieve above-average returns, you will not need to</p>
    </div>

    <div class="column right-b">
      <p>worry about attracting capital.</p>
      <p>A good rule of thumb is to aim for 24% annual return (~2% per month). This is considered a very good performance, and if you can match it with 2/1 annual return to Drawdown ratio, you're in the money!</p>
      <p class="note">Note — Annual return to Drawdown ratio of 2/1 means that if you make 20% annual return, your max drawdown does not exceed 10%.</p>
      <p>Even if you achieve this level of return on a small $1,000 account, this can actually be viewed favourably by investors as it shows that you can control your emotions and you are not greedy.</p>
      <p>So: <strong>First, learn to trade!</strong> Build a solid track record and you will never need to worry about funding. Till then, trade well &amp; trade safe.</p>
    </div>

    <div class="signoff">
      <strong>Devan R Kalmath</strong><br>
      Founder<br>
      <strong>Velmaro Crest Group</strong>
    </div>
  </section>
</body>
</html>
```